Business Card Design with new logo

Dorian Pelleway 4172
E 118th St Fernhollow, IL 62999
Cell: 217-555-0193
pellewayrestoration@mailvane.test

Classic Car Restoration Services Buy Sell Trade Consign

Dorian Pelleway 9698
Cell: 217-555-0193

```html
<!DOCTYPE html>
<html lang="en">
<head>
<meta charset="utf-8">
<title>Pelleway Restoration – Business Card</title>
<link href="https://fonts.googleapis.com/css2?family=Roboto:ital,wght@0,400;0,500;0,700;0,900;1,400&display=swap" rel="stylesheet">
<style>
  :root {
    --bg: #2a2c30;
    --navy: #1b2838;
    --red: #e2322c;
    --red-deep: #b81d22;
    --white: #ffffff;
    --ink: #1c1c1c;
  }
  * { box-sizing: border-box; margin: 0; padding: 0; }
  html, body {
    width: 1200px; height: 900px; overflow: hidden;
    background: var(--bg);
    font-family: "Roboto", sans-serif;
  }
  .stage {
    width: 1200px; height: 900px;
    display: flex; align-items: center; justify-content: center; gap: 50px;
  }
  .card {
    position: relative;
    width: 520px; height: 297px;
    border-radius: 18px;
    overflow: hidden;
  }

  /* Front */
  .card-front { background: var(--white); }
  .front-top {
    position: absolute; left: 0; top: 0; width: 100%; height: 78px;
    background: var(--navy);
  }
  .front-top .notch {
    position: absolute; bottom: -10px; left: 190px; width: 0; height: 0;
    border-left: 10px solid transparent; border-right: 10px solid transparent;
    border-top: 10px solid var(--navy);
  }
  .front-bottom {
    position: absolute; left: 0; bottom: 0; width: 100%; height: 74px;
    background: var(--red-deep);
  }
  .front-bottom .notch {
    position: absolute; top: -10px; left: 410px; width: 0; height: 0;
    border-left: 10px solid transparent; border-right: 10px solid transparent;
    border-bottom: 10px solid var(--red-deep);
  }
  .employee {
    position: absolute; right: 26px; top: 22px; text-align: right;
  }
  .employee-name {
    color: var(--red); font-weight: 700; font-size: 20px; letter-spacing: 0.5px;
  }
  .employee-role { color: var(--white); font-size: 14px; margin-top: 2px; }
  .brand {
    position: absolute; left: 28px; top: 98px; width: 175px;
    display: flex; align-items: center; gap: 8px;
  }
  .brand-dot { width: 14px; height: 14px; border-radius: 50%; background: var(--red); flex: none; }
  .brand-name {
    color: var(--navy); font-weight: 900; font-size: 17px; line-height: 1.15;
    text-transform: uppercase; letter-spacing: 0.5px;
  }
  .contact {
    position: absolute; left: 220px; top: 94px; right: 16px;
    color: var(--ink); font-size: 14px; line-height: 1.5;
  }
  .contact-line { display: flex; align-items: center; gap: 8px; white-space: nowrap; }
  .contact-line svg { width: 13px; height: 13px; flex: none; }
  .address { margin-top: 4px; }

  /* Back */
  .card-back { background: var(--navy); }
  .back-name {
    position: absolute; left: 0; top: 40px; width: 100%; text-align: center;
    color: var(--red); font-weight: 900; font-size: 64px; letter-spacing: 2px;
  }
  .tagline {
    position: absolute; left: 0; top: 150px; width: 100%;
    display: flex; align-items: center; justify-content: center; gap: 14px;
  }
  .tagline .rule { width: 70px; height: 2px; background: var(--red); }
  .tagline-text { text-align: center; color: var(--white); }
  .tagline-title { font-size: 19px; font-weight: 500; }
  .tagline-sub { font-size: 14px; font-style: italic; margin-top: 4px; }
  .back-edge {
    position: absolute; left: 0; bottom: 18px; width: 100%; height: 2px;
    background: var(--red);
  }
</style>
</head>
<body>
<main class="stage">
  <section class="card card-front" aria-label="Business card front">
    <div class="front-top">
      <span class="notch"></span>
      <div class="employee">
        <div class="employee-name">EMPLOYEE NAME</div>
        <div class="employee-role">manager</div>
      </div>
    </div>
    <div class="brand">
      <span class="brand-dot"></span>
      <span class="brand-name">Pelleway<br>Restoration LLC</span>
    </div>
    <div class="contact">
      <div class="contact-line">
        <svg viewBox="0 0 12 14" aria-hidden="true"><rect x="2" y="0.5" width="8" height="13" rx="1.5" fill="none" stroke="#e2322c" stroke-width="1.4"/></svg>
        217-555-0193
      </div>
      <div class="contact-line">
        <svg viewBox="0 0 14 11" aria-hidden="true"><rect x="0.5" y="0.5" width="13" height="10" fill="#e2322c"/><path d="M0.5 0.5 L7 6 L13.5 0.5" fill="none" stroke="#fff" stroke-width="1.2"/></svg>
        pellewayrestoration@mailvane.test
      </div>
      <div class="address">Dorian Pelleway 4172<br>E 118th St Fernhollow, IL 62999</div>
    </div>
    <div class="front-bottom"><span class="notch"></span></div>
  </section>

  <section class="card card-back" aria-label="Business card back">
    <div class="back-name">PELLEWAY</div>
    <div class="tagline">
      <span class="rule"></span>
      <div class="tagline-text">
        <div class="tagline-title">Classic Car Restoration Services</div>
        <div class="tagline-sub">Buy, Sell, Trade, Consign</div>
      </div>
      <span class="rule"></span>
    </div>
    <div class="back-edge"></div>
  </section>
</main>
</body>
</html>
```